Business Card Design for company

We want new business cards. We'd like something different-- yet still highly professional. Our tagline is Guiding strategy, building lasting results. Stock photos are ok, as long as they are relevant and look upscale.

Target Market(s)

Architecture/Business Management Consulting/Engineering Consulting

Contact Information for Business Card

dark gray background with pops of blue might be good, but you tell me. You're the designers. Rounded corners might be nice, but again, you tell me.

Font styles to use
Serif
Sans Serif

Colors
3276b5
5c5c5c
9d9d9d
fbfbfb

Requirements
Nice to have
• Something different, but still very professional.

```html
<!DOCTYPE html>
<html lang="en">
<head>
<meta charset="utf-8">
<title>Halvern Partners – Business Cards</title>
<link href="https://fonts.googleapis.com/css2?family=Montserrat:wght@400;500;600;700&display=swap" rel="stylesheet">
<style>
  :root {
    --stage: #151515;
    --brand-blue: #235a8f;
    --brand-blue-light: #2a66a0;
    --accent-blue: #2a5f98;
    --ink-gray: #4a4a4a;
    --mid-gray: #5c5c5c;
    --soft-gray: #d7d7d9;
    --paper: #f3f3f3;
    --white: #fbfbfb;
  }
  * { box-sizing: border-box; margin: 0; padding: 0; }
  html, body {
    width: 1200px; height: 900px; overflow: hidden;
    background: var(--stage);
    font-family: "Montserrat", Arial, sans-serif;
  }
  .card {
    position: absolute;
    width: 540px; height: 310px;
    border-radius: 24px;
    overflow: hidden;
  }

  /* Back of card */
  .card--back {
    left: 60px; top: 130px;
    background: linear-gradient(160deg, var(--brand-blue) 0%, var(--brand-blue-light) 100%);
  }
  .card--back .wordmark {
    position: absolute; left: 0; right: 0; top: 92px;
    text-align: center;
    color: var(--soft-gray);
    font-weight: 600;
    font-size: 36px;
    letter-spacing: 3px;
    text-transform: uppercase;
    line-height: 1;
  }
  .card--back .tagline-row {
    position: absolute; left: 0; right: 0; top: 196px;
    display: flex; align-items: center; gap: 14px;
  }
  .card--back .tagline-rule {
    flex: 1; height: 3px; background: var(--white);
  }
  .card--back .tagline {
    color: var(--white);
    font-size: 15px; font-weight: 400;
    letter-spacing: 0.5px;
    white-space: nowrap;
  }

  /* Front of card */
  .card--front {
    left: 600px; top: 450px;
    background: linear-gradient(135deg, var(--white) 0%, var(--paper) 100%);
  }
  .card--front .wordmark {
    position: absolute; right: 34px; top: 40px;
    color: var(--accent-blue);
    font-weight: 600;
    font-size: 24px;
    letter-spacing: 2px;
    text-transform: uppercase;
  }
  .card--front .top-rule {
    position: absolute; left: 206px; right: 34px; top: 112px;
    height: 1px; background: var(--accent-blue);
  }
  .person {
    position: absolute; left: 34px; top: 148px;
  }
  .person__name {
    color: var(--accent-blue);
    font-weight: 700; font-size: 21px;
    letter-spacing: 1px; text-transform: uppercase;
  }
  .person__title {
    color: var(--ink-gray);
    font-size: 15px; margin-top: 2px;
  }
  .person__rule {
    width: 220px; height: 1px; background: var(--accent-blue); margin-top: 10px;
  }
  .contacts {
    position: absolute; left: 34px; top: 214px;
    list-style: none;
    color: var(--ink-gray); font-size: 13px;
  }
  .contacts li {
    display: flex; align-items: center; gap: 8px; line-height: 20px;
  }
  .contacts svg { width: 12px; height: 12px; fill: var(--accent-blue); flex: none; }
  .address {
    position: absolute; right: 34px; top: 218px;
    color: var(--ink-gray); font-size: 13px; line-height: 20px;
    font-style: normal; text-align: left;
  }
  .base-band {
    position: absolute; left: 0; right: 0; bottom: 0; height: 10px;
    display: flex;
  }
  .base-band__blue { flex: 0 0 64%; background: var(--accent-blue); }
  .base-band__gray { flex: 1; background: var(--mid-gray); }
</style>
</head>
<body>

<section class="card card--back" aria-label="Card back">
  <div class="wordmark">Halvern Partners</div>
  <div class="tagline-row">
    <span class="tagline-rule"></span>
    <span class="tagline">Guiding strategy, building lasting results</span>
    <span class="tagline-rule"></span>
  </div>
</section>

<section class="card card--front" aria-label="Card front">
  <div class="wordmark">Halvern Partners</div>
  <div class="top-rule"></div>

  <div class="person">
    <div class="person__name">Daniel Reeve</div>
    <div class="person__title">CEO &amp; Founder</div>
    <div class="person__rule"></div>
  </div>

  <ul class="contacts">
    <li>
      <svg viewBox="0 0 24 24" aria-hidden="true"><path d="M6.6 10.8a15 15 0 0 0 6.6 6.6l2.2-2.2a1 1 0 0 1 1-.25 11.4 11.4 0 0 0 3.6.57 1 1 0 0 1 1 1V20a1 1 0 0 1-1 1A17 17 0 0 1 3 4a1 1 0 0 1 1-1h3.5a1 1 0 0 1 1 1c0 1.25.2 2.45.57 3.57a1 1 0 0 1-.25 1z"/></svg>
      (555) 014.276
    </li>
    <li>
      <svg viewBox="0 0 24 24" aria-hidden="true"><path d="M2 5h20v14H2zm2 2v.5l8 5 8-5V7zm0 2.8V17h16V9.8l-8 5z"/></svg>
      info@halvernpartners.com
    </li>
    <li>
      <svg viewBox="0 0 24 24" aria-hidden="true"><circle cx="12" cy="12" r="10"/></svg>
      www.halvernpartners.com
    </li>
  </ul>

  <address class="address">
    820 W. Cedar St Suite 210<br>
    Avondale, OR 97301
  </address>

  <div class="base-band">
    <span class="base-band__blue"></span>
    <span class="base-band__gray"></span>
  </div>
</section>

</body>
</html>
```